Power Scout with goTurn messages

Power Scout is an energy switching platform, which automatically switches you to the best energy tariff. All messages are attached.

Target Market(s)

austria

Number of Pages Required

4 page

```html
<!DOCTYPE html>
<html lang="en">
<head>
<meta charset="utf-8">
<title>Power Scout – Energy switching</title>
<link href="https://fonts.googleapis.com/css2?family=Poppins:wght@400;500;600;700&display=swap" rel="stylesheet">
<style>
:root{
  --navy:#0f1a31;
  --navy-2:#18264a;
  --orange:#f6a21a;
  --orange-dark:#e48c06;
  --ink:#1d1f26;
  --text:#5c6070;
  --muted:#9a9eab;
  --line:#e7e8ee;
  --card-dark:#23262d;
  --ribbon:#e8424f;
  --soft:#f4f5f9;
  --white:#ffffff;
}
*{box-sizing:border-box;margin:0;padding:0}
html,body{width:1200px;height:4824px;overflow:hidden}
body{font-family:"Poppins",sans-serif;color:var(--text);background:var(--white);position:relative;font-size:15px;line-height:1.7}
.section{position:absolute;left:0;width:1200px}
.btn{display:inline-block;background:var(--orange);color:var(--white);font-weight:600;font-size:12px;letter-spacing:1px;text-transform:uppercase;padding:12px 24px;border-radius:3px}
.btn-dark{background:var(--navy-2)}
.heading{color:var(--ink);font-weight:600;font-size:40px;line-height:1.2;text-align:center}
.lead{font-size:14px;text-align:center;width:760px;margin:18px auto 0;color:var(--text)}
.art{position:absolute;border-radius:12px}

/* hero */
.hero{top:0;height:900px}
.hero-bg{position:absolute;inset:0}
.nav{position:absolute;top:20px;left:48px;right:48px;height:60px;display:flex;align-items:center}
.brand{display:flex;align-items:center;gap:10px;font-weight:700;font-size:26px;color:var(--orange)}
.brand-dot{width:14px;height:14px;border-radius:50%;background:var(--orange)}
.nav-links{margin-left:auto;display:flex;gap:44px;color:var(--white);font-size:15px;font-weight:500;align-items:center}
.nav-links .btn{padding:9px 22px;font-size:13px;letter-spacing:0;text-transform:none}
.hero-copy{position:absolute;left:48px;top:150px;width:560px;color:var(--white)}
.hero-copy h1{font-size:54px;font-weight:700;line-height:1.18}
.hero-copy p{margin-top:26px;font-size:16px;color:#cfd5e4;width:440px}
.hero-copy .btn{margin-top:34px}
.hero-art{left:640px;top:110px;width:520px;height:520px;border-radius:50%;background:radial-gradient(circle at 50% 45%,#2f4476,#182850 70%)}

/* register */
.register{top:940px;height:440px}
.features{display:flex;gap:46px;justify-content:center;margin-top:44px}
.feature{width:300px;height:240px;background:var(--white);box-shadow:0 6px 30px rgba(20,30,60,.08);text-align:center;padding-top:30px}
.feature-icon{width:84px;height:84px;border-radius:50%;background:#3a3d46;margin:0 auto;display:flex;align-items:center;justify-content:center}
.feature.is-active .feature-icon{background:var(--orange)}
.feature h3{color:var(--ink);font-size:18px;font-weight:600;margin-top:16px}
.feature p{font-size:13px;width:220px;margin:6px auto 0;line-height:1.6}

/* never pay */
.save{top:1410px;height:460px}
.save-copy{position:absolute;left:170px;top:40px;width:430px}
.save-copy h2{color:var(--ink);font-size:38px;font-weight:600;line-height:1.2}
.save-copy p{font-size:13px;margin-top:18px}
.save-copy .btn{margin-top:26px}
.save-art{left:630px;top:0;width:550px;height:440px;background:linear-gradient(135deg,#e9edf7,#cfd8ee)}
.deco-ring{position:absolute;border-radius:50%;border:18px solid #eceaf6}

/* how */
.how{top:1880px;height:790px}
.phone{position:absolute;left:210px;top:40px;width:300px;height:600px;border-radius:42px;background:#141414;padding:14px}
.phone-screen{width:100%;height:100%;border-radius:30px;background:var(--white);overflow:hidden;position:relative}
.phone-bar{height:58px;display:flex;align-items:center;justify-content:center;font-size:12px;color:var(--ink);font-weight:600;border-bottom:1px solid var(--line)}
.phone-photo{position:absolute;top:58px;left:0;right:0;bottom:0;background:linear-gradient(160deg,#f3b935,#c98a17 60%,#6b5a3a)}
.how-copy{position:absolute;left:610px;top:70px;width:420px}
.how-copy h2{color:var(--ink);font-size:38px;font-weight:600;line-height:1.2}
.how-copy > p{font-size:13px;margin-top:16px}
.step{display:flex;gap:22px;margin-top:30px}
.step-icon{flex:none;width:60px;height:60px;border-radius:50%;background:#fdf0d6;display:flex;align-items:center;justify-content:center}
.step h4{color:var(--ink);font-size:16px;font-weight:600}
.step p{font-size:13px;line-height:1.55;margin-top:4px}
.how-copy .btn{margin-top:34px}

/* cheapest */
.cheap{top:2690px;height:520px}
.cheap-art{left:0;top:0;width:640px;height:500px;border-radius:0 12px 12px 0;background:linear-gradient(180deg,#eef1f6,#c9d5e6 70%,#8fb06d)}
.cheap-copy{position:absolute;left:680px;top:100px;width:420px}
.cheap-copy h2{color:var(--ink);font-size:40px;font-weight:600;line-height:1.2}
.cheap-copy .intro{color:var(--ink);font-size:14px;font-weight:600;margin-top:22px}
.ticks{list-style:none;margin-top:10px}
.ticks li{font-size:13px;padding-left:22px;position:relative;margin-top:8px;line-height:1.5}
.ticks li::before{content:"";position:absolute;left:0;top:6px;width:8px;height:8px;border-radius:50%;background:var(--orange)}

/* pricing */
.pricing{top:3230px;height:660px}
.plans{display:flex;justify-content:center;align-items:center;margin-top:46px}
.plan{width:330px;height:390px;background:var(--card-dark);color:#c9ccd4;padding:36px 40px;border-radius:6px;position:relative}
.plan h3{font-size:17px;color:var(--white);font-weight:600}
.plan .sub{font-size:12px;color:var(--muted)}
.price{font-size:34px;font-weight:700;color:var(--white);margin-top:16px}
.price small{font-size:14px;font-weight:500}
.plan ul{list-style:none;margin-top:20px;font-size:13px}
.plan li{margin-top:10px}
.plan .btn{margin-top:26px;padding:10px 24px}
.plan.is-featured{width:330px;height:460px;background:var(--white);color:var(--text);box-shadow:0 12px 40px rgba(15,20,40,.2);text-align:center;z-index:2;overflow:hidden;margin:0 -6px}
.plan.is-featured h3,.plan.is-featured .price{color:var(--ink)}
.plan.is-featured .btn{background:var(--ink)}
.ribbon{position:absolute;top:30px;left:-48px;width:200px;transform:rotate(-45deg);background:var(--ribbon);color:var(--white);font-size:10px;font-weight:600;text-align:center;padding:4px 0;letter-spacing:1px}

/* testimonial */
.reviews{top:3910px;height:630px}
.reviews .heading{width:560px;margin:0 auto}
.map{left:150px;top:150px;width:900px;height:440px;background:radial-gradient(ellipse at center,#f2f3f6,#fafbfc 70%,transparent)}
.avatar{position:absolute;left:540px;top:190px;width:120px;height:120px;border-radius:50%;background:linear-gradient(135deg,#d9c4b0,#a98a74);border:6px solid var(--white);box-shadow:0 6px 24px rgba(0,0,0,.1)}
.quote-mark{position:absolute;left:532px;top:210px;width:30px;height:30px;border-radius:50%;background:var(--orange);color:var(--white);font-weight:700;font-size:20px;text-align:center;line-height:38px}
.quote{position:absolute;left:190px;top:340px;width:820px;text-align:center;font-style:italic;font-size:16px;line-height:1.75}
.quote-name{position:absolute;left:0;right:0;top:490px;text-align:center;color:var(--ink);font-weight:600;font-size:20px}
.quote-role{position:absolute;left:0;right:0;top:524px;text-align:center;font-size:12px;color:var(--muted)}
.arrow{position:absolute;top:300px;width:60px;height:60px;border-radius:50%;background:var(--orange);display:flex;align-items:center;justify-content:center}

/* footer */
.footer{top:4560px;height:264px;background:var(--soft)}
.footer-cols{display:flex;padding:30px 80px 0;gap:70px}
.footer-col h5{color:var(--ink);font-size:16px;font-weight:600;margin-bottom:10px}
.footer-col p,.footer-col li{font-size:12px;line-height:1.9;list-style:none}
.footer-col li.is-current{color:var(--orange)}
.footer-about{width:250px}
.footer-about .brand{font-size:24px;margin-bottom:8px}
.footer-bar{position:absolute;left:80px;right:80px;bottom:0;height:40px;border-top:1px solid var(--line);display:flex;align-items:center;font-size:11px;color:var(--muted)}
.footer-bar nav{margin-left:auto;display:flex;gap:22px}
</style>
</head>
<body>

<header class="section hero">
  <svg class="hero-bg" width="1200" height="900" viewBox="0 0 1200 900" aria-hidden="true">
    <path d="M0 0H1200V760C1050 880 870 820 700 740C520 660 380 700 240 760C140 800 60 800 0 780Z" fill="#0f1a31"/>
    <circle cx="1130" cy="560" r="22" fill="#f6a21a" opacity=".9"/>
    <circle cx="70" cy="620" r="8" fill="#f6a21a"/>
  </svg>
  <div class="nav">
    <div class="brand"><span class="brand-dot"></span>Power Scout</div>
    <nav class="nav-links">
      <span>Home</span><span>Features</span><span>Process</span><span>Discover</span><span>Feedback</span>
      <span class="btn">Sign Up</span>
    </nav>
  </div>
  <div class="hero-copy">
    <h1>Immer automatisch zum günstigsten Energieanbieter wechseln</h1>
    <p>Lorem ipsum dolor sit amet consectetur adipiscing elit sed do eiusmod tempor incididunt.</p>
    <span class="btn">Jetzt wechseln</span>
  </div>
  <div class="art hero-art" role="img" aria-label="Illustration of people lifting a glowing light bulb with plants and energy symbols"></div>
</header>

<section class="section register">
  <h2 class="heading">Register once, always save</h2>
  <p class="lead">On the other hand we denounce with righteous indignation and dislike men who are so beguiled and demoralized by the charms of pleasure of the moment so blinded by desire that they cannot foresee the pain.</p>
  <div class="features">
    <div class="feature">
      <div class="feature-icon"><svg width="40" height="40" viewBox="0 0 40 40"><path d="M10 26a7 7 0 0 1 1-14 9 9 0 0 1 17 2 6 6 0 0 1 2 12Z" fill="#fff"/></svg></div>
      <h3>Independently</h3>
      <p>We work only for you, in order to remain independent.</p>
    </div>
    <div class="feature is-active">
      <div class="feature-icon"><svg width="40" height="40" viewBox="0 0 40 40"><path d="M20 5l13 5v9c0 8-6 14-13 16C13 33 7 27 7 19v-9Z" fill="#fff"/><path d="M14 20l4 4 8-8" stroke="#f6a21a" stroke-width="3" fill="none"/></svg></div>
      <h3>Automatically</h3>
      <p>You sign up once and we'll do the rest. All automatically.</p>
    </div>
    <div class="feature">
      <div class="feature-icon"><svg width="40" height="40" viewBox="0 0 40 40"><path d="M20 4c6 5 8 12 6 20h-12c-2-8 0-15 6-20Z" fill="#fff"/><path d="M14 24l-5 8 6-2M26 24l5 8-6-2" fill="#fff"/><circle cx="20" cy="15" r="3" fill="#3a3d46"/></svg></div>
      <h3>Fair</h3>
      <p>Power Scout always stays fair. Despite service charge.</p>
    </div>
  </div>
</section>

<section class="section save">
  <div class="deco-ring" style="left:330px;top:-20px;width:120px;height:120px"></div>
  <div class="save-copy">
    <h2>Never pay too much for electricity &amp; gas again</h2>
    <p>Gone are the days of bad deals, tedious rate comparison and boring exchange forms.</p>
    <p>With the automatic change service for Power Scout you will never again pay too much for electricity and gas. And that without lifting a finger. We fight for you through the tariff jungle.</p>
    <p>So save your hard-earned money and become a Power Scout.</p>
    <span class="btn btn-dark">Learn more ›</span>
  </div>
  <div class="art save-art" role="img" aria-label="Illustration of people around a large smartphone with a rising bar chart and coins"></div>
</section>

<section class="section how">
  <div class="phone">
    <div class="phone-screen">
      <div class="phone-bar">Power Scout</div>
      <div class="phone-photo" role="img" aria-label="Photo of an engineer working on electrical equipment"></div>
    </div>
  </div>
  <div class="how-copy">
    <h2>How do I become Power Scout?</h2>
    <p>Lorem ipsum dolor sit amet consectetur adipiscing elit sed do eiusmod tempor incididunt ut labore et dolore magna aliqua. Ut enim ad minim veniam quis nostrud exercitation ullamco.</p>
    <div class="step">
      <div class="step-icon"><svg width="28" height="28" viewBox="0 0 28 28"><circle cx="14" cy="10" r="5" fill="#f6a21a"/><path d="M4 26c1-6 5-9 10-9s9 3 10 9Z" fill="#f6a21a"/></svg></div>
      <div><h4>Once login</h4><p>Upload financial statements. Select preferences. Finish the registration.</p></div>
    </div>
    <div class="step">
      <div class="step-icon"><svg width="28" height="28" viewBox="0 0 28 28"><path d="M16 2L6 16h7l-2 10 11-15h-7Z" fill="#f6a21a"/></svg></div>
      <div><h4>Automatic</h4><p>Take charge! We pick the cheapest fare for you and carry out the change automatically.</p></div>
    </div>
    <div class="step">
      <div class="step-icon"><svg width="28" height="28" viewBox="0 0 28 28"><rect x="3" y="8" width="22" height="15" rx="3" fill="#f6a21a"/><circle cx="14" cy="15.5" r="3.5" fill="#fff"/></svg></div>
      <div><h4>Sit back and save money</h4><p>Always switch automatically to the low fare.</p></div>
    </div>
    <span class="btn">Learn more ›</span>
  </div>
</section>

<section class="section cheap">
  <div class="art cheap-art" role="img" aria-label="Illustration of solar panels, a wind turbine and power pylons"></div>
  <div class="cheap-copy">
    <h2>The cheapest of all super powers</h2>
    <p class="intro">From 24 euros you are there:</p>
    <ul class="ticks">
      <li>Service fee electricity or gas (1 meter): 24 euros / year</li>
      <li>Service fee electricity and gas (2 counters): 36 Euro / year</li>
      <li>The first fee will be charged only after your first change</li>
      <li>Save up to 350 euros annually electricity and gas costs at the first change *</li>
    </ul>
  </div>
</section>

<section class="section pricing">
  <h2 class="heading">Service fee in the year</h2>
  <p class="lead">On the other hand we denounce with righteous indignation and dislike men who are so beguiled and demoralized by the charms of pleasure of the moment so blinded by desire that they cannot foresee the pain.</p>
  <div class="plans">
    <div class="plan">
      <h3>Basic Package</h3><p class="sub">On the other hand</p>
      <p class="price">€125<small>/mo.</small></p>
      <ul><li>Free Client Support</li><li>Easy Implementation</li><li>Great Privacy Policy</li></ul>
      <span class="btn">Buy now</span>
    </div>
    <div class="plan is-featured">
      <span class="ribbon">POPULAR</span>
      <h3>Advanced Package</h3><p class="sub">On the other hand</p>
      <p class="price">€440<small>/mo.</small></p>
      <ul><li>Free Client Support</li><li>Easy Implementation</li><li>Great Privacy Policy</li><li>Top Notch Experience</li><li>Website and app designing</li></ul>
      <span class="btn">Buy now</span>
    </div>
    <div class="plan">
      <h3>Premium Package</h3><p class="sub">On the other hand</p>
      <p class="price">€155<small>/mo.</small></p>
      <ul><li>Free Client Support</li><li>Easy Implementation</li><li>Great Privacy Policy</li><li>Content development</li></ul>
      <span class="btn">Buy now</span>
    </div>
  </div>
</section>

<section class="section reviews">
  <h2 class="heading">Check What Our Client Says About Our App</h2>
  <div class="art map" role="img" aria-label="Faint world map in the background"></div>
  <div class="avatar" role="img" aria-label="Portrait of the quoted managing director"></div>
  <div class="quote-mark">“</div>
  <div class="arrow" style="left:90px"><svg width="20" height="20" viewBox="0 0 20 20"><path d="M13 3L6 10l7 7" stroke="#fff" stroke-width="3" fill="none"/></svg></div>
  <div class="arrow" style="right:90px"><svg width="20" height="20" viewBox="0 0 20 20"><path d="M7 3l7 7-7 7" stroke="#fff" stroke-width="3" fill="none"/></svg></div>
  <p class="quote">Marlene Hofbauer-Lind is the founder of the Clearwave Group. Due to her many years of experience in the energy industry, including as head of Alpenstrom Vertrieb GmbH and the Alpine Climate Fund as well as Nordwerk AG (Sector Cluster Lead Energy), she has sound knowledge of the Austrian energy market.</p>
  <p class="quote-name">Marlene Hofbauer-Lind</p>
  <p class="quote-role">Managing Director</p>
</section>

<footer class="section footer">
  <div class="footer-cols">
    <div class="footer-col footer-about">
      <div class="brand"><span class="brand-dot"></span>Power Scout</div>
      <p>The overwhelming majority of Austrians remain with the same energy provider year after year. And that, without knowing if they really get the best price.</p>
    </div>
    <div class="footer-col">
      <h5>New Business</h5>
      <p>Power Scout GmbH<br>Lindengasse 12<br>1070 Wien<br>Phone +43 1 555 0123<br>Mail hello@powerscout.at</p>
    </div>
    <div class="footer-col">
      <h5>Features</h5>
      <ul><li>Modules</li><li class="is-current">Client Business</li><li>Download</li><li>Pricing</li></ul>
    </div>
    <div class="footer-col">
      <h5>Our Company</h5>
      <ul><li>Our Team</li><li>Testimonial</li><li>Partners</li><li>Work Life</li><li>Contact Us</li></ul>
    </div>
  </div>
  <div class="footer-bar">
    <span>Power Scout 2019. All Rights Reserved.</span>
    <nav><span>About</span><span>Help</span><span>Terms</span><span>Privacy</span></nav>
  </div>
</footer>

</body>
</html>
```